Startup photo studio needs full suite design (logo, business cards, etc) starting with a website.

We need a website designed for a startup photo studio in the Sacramento area called Silver Lantern Photo Studio. We do portrait work, specializing in the male form and are looking to get into editorial. We would also like to be able to sell prints, posters and canvasses of our work. I would like an elegant but fun design. One of the most important things a portrait photographer needs is the trust of the model. The website would convey honesty, friendliness and warmth as well. I have a domain name with NetHarbor, silverlanternstudio.example email address should be my name with that domain.

Target Market(s)

Art enthusiasts, business portraits, online dating photos

Industry/Entity Type

Professional Photography

Contact Information for Business Card

Simple please. Just logo and contact info. Phone, email, website. no address required

Logo Text

Silver Lantern Photo Studio --- light tells the story

Number of Pages Required

3 page

Font styles to use
Sans Serif

Colors

Designer to choose colors to be used in the design.

Requirements
Must have
• Simple clean design.
Nice to have
• Somehow one of my photos in the design? maybe not...
Should not have
• No weddings!

```html
<!DOCTYPE html>
<html lang="en">
<head>
<meta charset="utf-8">
<title>Silver Lantern Studio</title>
<link href="https://fonts.googleapis.com/css2?family=Roboto+Slab:wght@400&family=Montserrat:wght@400;500;600&family=Open+Sans:wght@400;600&display=swap" rel="stylesheet">
<style>
:root{
  --orange:#f07320;
  --blue:#2f78b9;
  --blue-mid:#2b6aa8;
  --ink:#333333;
  --text:#555555;
  --light:#f6f7f9;
  --footer:#3a3a3a;
  --white:#ffffff;
  --photo-grey:#7b7f84;
  --photo-dark:#24262b;
  --photo-soft:#9aa3ad;
}
*{margin:0;padding:0;box-sizing:border-box}
html,body{width:1200px;height:2830px;overflow:hidden}
body{position:relative;background:var(--white);font-family:"Open Sans",Arial,sans-serif;color:var(--text)}
.abs{position:absolute}
.site-header{left:0;top:0;width:1200px;height:100px;background:var(--white)}
.brand{left:85px;top:32px;font-family:"Roboto Slab",Georgia,serif;font-weight:400;font-size:28px;color:var(--ink);white-space:nowrap}
.nav a{position:absolute;top:43px;font-family:"Montserrat",Arial,sans-serif;font-size:12px;color:var(--ink);text-decoration:none;white-space:nowrap}
.nav a.active{color:var(--orange)}
.hero{left:0;top:100px;width:1200px;height:506px;background:linear-gradient(90deg,#84888c 0%,#6c7074 100%)}
.hero h1{left:113px;top:142px;font-family:"Montserrat",Arial,sans-serif;font-weight:500;font-size:25px;color:var(--white)}
.hero p{left:113px;top:198px;width:372px;font-size:11.5px;line-height:25px;color:var(--white)}
.btn{display:block;background:var(--orange);color:var(--white);font-family:"Montserrat",Arial,sans-serif;font-weight:500;text-align:center}
.hero .btn{left:111px;top:325px;width:129px;height:41px;line-height:41px;font-size:14px}
.arrow{width:52px;height:52px;border:2px solid var(--white);border-radius:50%;top:227px}
.about{left:0;top:606px;width:1200px;height:366px;background:var(--orange)}
.about-photo{left:85px;top:642px;width:338px;height:394px;background:var(--white);box-shadow:0 6px 10px rgba(0,0,0,.18);padding:8px}
.about-photo div{width:100%;height:100%;background:var(--photo-dark)}
.about h2{left:481px;top:48px;font-family:"Montserrat",Arial,sans-serif;font-size:28px;font-weight:500;color:var(--white)}
.about p{left:481px;width:575px;font-size:11.5px;line-height:26px;color:var(--white)}
.section-title{width:1200px;left:0;text-align:center;font-family:"Montserrat",Arial,sans-serif;font-size:25px;font-weight:500;color:var(--ink)}
.works{left:0;top:972px;width:1200px;height:868px;background:var(--light)}
.work{top:158px;width:330px;text-align:center}
.work .circle{width:114px;height:114px;border-radius:50%;margin:0 auto;display:flex;align-items:center;justify-content:center}
.work h3{margin-top:18px;font-family:"Montserrat",Arial,sans-serif;font-size:17px;font-weight:500;color:var(--blue)}
.work.orange h3{color:var(--orange)}
.work p{margin-top:8px;font-size:11.5px;line-height:26px;color:var(--text)}
.rule{left:85px;top:439px;width:1030px;height:1px;background:#e6e7ea}
.session h2{left:85px;top:486px;font-family:"Montserrat",Arial,sans-serif;font-size:20px;font-weight:500;color:var(--ink)}
.rates{left:85px;top:527px;font-family:"Montserrat",Arial,sans-serif;font-size:11px;font-weight:600;color:var(--orange);white-space:nowrap}
.features{left:85px;top:572px;list-style:none}
.features li{height:37px;font-size:11.5px;color:var(--text);display:flex;align-items:center}
.features svg{margin-right:14px;flex:none}
.session-photo{left:657px;top:490px;width:449px;height:325px;background:var(--white);padding:7px;box-shadow:0 0 4px rgba(0,0,0,.12)}
.session-photo div{width:100%;height:100%;background:var(--photo-soft)}
.contact{left:0;top:1840px;width:1200px;height:355px;background:var(--blue)}
.contact h2{top:36px;color:var(--white)}
.contact .lead{top:80px;width:1200px;text-align:center;font-size:11.5px;color:var(--white)}
.field{background:var(--white);font-size:11px;color:var(--ink);padding:10px 12px}
.submit{left:534px;top:285px;width:132px;height:39px;line-height:39px;font-size:14px}
.gallery-title{top:2222px;color:var(--orange)}
.tabs span{position:absolute;top:2277px;font-family:"Montserrat",Arial,sans-serif;font-size:12px;color:var(--ink);white-space:nowrap}
.tabs span.active{color:var(--orange)}
.tile{position:absolute;background:var(--photo-grey)}
.tile.dark{background:var(--photo-dark)}
.tile.soft{background:var(--photo-soft)}
.footer{left:0;top:2761px;width:1200px;height:69px;background:var(--footer)}
.footer p{left:85px;top:26px;font-size:11.5px;color:var(--white)}
.social{top:16px;width:36px;height:36px;border:2px solid var(--white);border-radius:50%}
</style>
</head>
<body>

<header class="abs site-header">
  <div class="abs brand">Silver Lantern Studio</div>
  <nav class="nav">
    <a class="active" style="left:604px">HOME</a>
    <a style="left:698px">ABOUT US</a>
    <a style="left:817px">PRICING</a>
    <a style="left:923px">GALLERY</a>
    <a style="left:1034px">CONTACT US</a>
  </nav>
</header>

<section class="abs hero" role="img" aria-label="Hero photograph: studio group portrait of three models">
  <h1 class="abs">SILVER LANTERN STUDIO</h1>
  <p class="abs">Sed ut perspiciatis unde omnis iste natus error sit voluptatem accusantium doloremque laudantium, totam rem aperiam, eaque ipsa quae ab illo inventore veritatis et quasi architecto beatae vitae dicta sunt totam rem iste natus error sit explicabo.</p>
  <span class="abs btn">READ MORE</span>
  <svg class="abs arrow" style="left:23px" viewBox="0 0 52 52"><path d="M29 17 L20 26 L29 35" fill="none" stroke="#fff" stroke-width="3"/></svg>
  <svg class="abs arrow" style="left:1121px" viewBox="0 0 52 52"><path d="M23 17 L32 26 L23 35" fill="none" stroke="#fff" stroke-width="3"/></svg>
</section>

<section class="abs about">
  <h2 class="abs">ABOUT US</h2>
  <svg class="abs" style="left:481px;top:100px" width="72" height="10" viewBox="0 0 72 10"><line x1="5" y1="5" x2="67" y2="5" stroke="#fff" stroke-width="1.5"/><circle cx="5" cy="5" r="3.5" fill="#f07320" stroke="#fff" stroke-width="1.5"/><circle cx="36" cy="5" r="3.5" fill="#f07320" stroke="#fff" stroke-width="1.5"/><circle cx="67" cy="5" r="3.5" fill="#f07320" stroke="#fff" stroke-width="1.5"/></svg>
  <p class="abs" style="top:133px">Silver Lantern began as a creative outlet and hobby. I have a long history, over 20 years, in printing and graphic arts so photography is a natural extension for this experienced eye</p>
  <p class="abs" style="top:209px">I specialize in the male form, leaning towards the artistic but portraits of all kinds are the real soul of the business. I have a passion for people! Prior to this career I was in the non-profit world advocating for the elderly. I feel this empathy gives me a unique ability to connect with models and draw out the best in them. I love people. I love making them look beautiful. Or professional, or datable, or simply happy."</p>
</section>
<div class="abs about-photo"><div role="img" aria-label="Portrait photograph of the photographer"></div></div>

<section class="abs works">
  <h2 class="abs section-title" style="top:66px">OUR WORKS</h2>
  <div class="abs work" style="left:86px">
    <div class="circle" style="background:var(--blue-mid)"><svg width="50" height="50" viewBox="0 0 50 50" fill="none" stroke="#fff" stroke-width="3"><rect x="15" y="8" width="20" height="10"/><rect x="7" y="18" width="36" height="16" rx="2" fill="#fff"/><rect x="15" y="30" width="20" height="12" fill="#2b6aa8"/></svg></div>
    <h3>PRINTS</h3>
    <p>Sed ut perspiciatis unde omnis iste natus error sit voluptatem accusantium doloremque laudantium, beatae vitae dicta sunt explicabo.</p>
  </div>
  <div class="abs work orange" style="left:437px">
    <div class="circle" style="background:var(--orange)"><svg width="50" height="50" viewBox="0 0 50 50" fill="none" stroke="#fff" stroke-width="3"><rect x="12" y="6" width="26" height="38"/><rect x="18" y="13" width="14" height="12"/><line x1="18" y1="31" x2="32" y2="31"/><line x1="18" y1="37" x2="32" y2="37"/></svg></div>
    <h3>POSTERS</h3>
    <p>Sed ut perspiciatis unde omnis iste natus error sit voluptatem accusantium doloremque laudantium, beatae vitae dicta sunt explicabo.</p>
  </div>
  <div class="abs work" style="left:788px">
    <div class="circle" style="background:var(--blue-mid)"><svg width="54" height="54" viewBox="0 0 54 54" fill="none" stroke="#fff" stroke-width="3"><line x1="6" y1="6" x2="48" y2="6"/><line x1="16" y1="6" x2="16" y2="14"/><line x1="38" y1="6" x2="38" y2="26"/><rect x="8" y="14" width="18" height="32"/><rect x="30" y="26" width="16" height="16"/><circle cx="38" cy="34" r="3"/></svg></div>
    <h3>CANVASSES</h3>
    <p>Sed ut perspiciatis unde omnis iste natus error sit voluptatem accusantium doloremque laudantium, beatae vitae dicta sunt explicabo.</p>
  </div>
  <div class="abs rule"></div>

  <div class="session">
    <h2 class="abs">STANDARD SESSION $450</h2>
    <div class="abs rates">PROFESSIONALS - $352 &nbsp;|&nbsp; DATING SITES - $250 &nbsp;|&nbsp; COUPLES - $155</div>
    <ul class="abs features">
      <li><svg width="12" height="12" viewBox="0 0 12 12"><circle cx="6" cy="6" r="4.5" fill="none" stroke="#f07320" stroke-width="1.6"/><circle cx="6" cy="6" r="1.6" fill="#f07320"/></svg>All sessions include photographer's time + talent, post processing of images</li>
      <li><svg width="12" height="12" viewBox="0 0 12 12"><circle cx="6" cy="6" r="4.5" fill="none" stroke="#f07320" stroke-width="1.6"/><circle cx="6" cy="6" r="1.6" fill="#f07320"/></svg>90 min session of photography time at a local studio or location</li>
      <li><svg width="12" height="12" viewBox="0 0 12 12"><circle cx="6" cy="6" r="4.5" fill="none" stroke="#f07320" stroke-width="1.6"/><circle cx="6" cy="6" r="1.6" fill="#f07320"/></svg>Final images fully edited (80-100)</li>
      <li><svg width="12" height="12" viewBox="0 0 12 12"><circle cx="6" cy="6" r="4.5" fill="none" stroke="#f07320" stroke-width="1.6"/><circle cx="6" cy="6" r="1.6" fill="#f07320"/></svg>Print release for personal use and personal reproduction</li>
      <li><svg width="12" height="12" viewBox="0 0 12 12"><circle cx="6" cy="6" r="4.5" fill="none" stroke="#f07320" stroke-width="1.6"/><circle cx="6" cy="6" r="1.6" fill="#f07320"/></svg>CD with all your high resolution images</li>
      <li><svg width="12" height="12" viewBox="0 0 12 12"><circle cx="6" cy="6" r="4.5" fill="none" stroke="#f07320" stroke-width="1.6"/><circle cx="6" cy="6" r="1.6" fill="#f07320"/></svg>Online password protected viewing gallery of all images</li>
      <li><svg width="12" height="12" viewBox="0 0 12 12"><circle cx="6" cy="6" r="4.5" fill="none" stroke="#f07320" stroke-width="1.6"/><circle cx="6" cy="6" r="1.6" fill="#f07320"/></svg>Travel fee's may apply</li>
    </ul>
    <div class="abs session-photo"><div role="img" aria-label="Session sample photograph: group portrait of three models"></div></div>
  </div>
</section>

<section class="abs contact">
  <h2 class="abs section-title" style="color:var(--white)">CONTACT FORM</h2>
  <p class="abs lead">Sed ut perspiciatis unde omnis iste natus error sit voluptatem accusantium doloremque laudantium</p>
  <div class="abs field" style="left:321px;top:117px;width:275px;height:40px">First Name :</div>
  <div class="abs field" style="left:604px;top:117px;width:275px;height:40px">Last Name :</div>
  <div class="abs field" style="left:321px;top:164px;width:275px;height:40px">Phone :</div>
  <div class="abs field" style="left:604px;top:164px;width:275px;height:40px">Email :</div>
  <div class="abs field" style="left:321px;top:211px;width:558px;height:61px">Message :</div>
  <span class="abs btn submit">SUBMIT</span>
</section>

<h2 class="abs section-title gallery-title">PHOTO GALLERY</h2>
<div class="tabs">
  <span class="active" style="left:410px">PORTRAITS</span>
  <span style="left:506px">|</span>
  <span style="left:543px">BOUDOIR</span>
  <span style="left:631px">|</span>
  <span style="left:667px">EDITORIAL/ARTISTIC</span>
</div>
<div class="tile" style="left:85px;top:2321px;width:247px;height:183px" role="img" aria-label="Gallery photograph: portrait"></div>
<div class="tile dark" style="left:85px;top:2519px;width:247px;height:183px" role="img" aria-label="Gallery photograph: group portrait"></div>
<div class="tile dark" style="left:347px;top:2321px;width:246px;height:381px" role="img" aria-label="Gallery photograph: portrait"></div>
<div class="tile soft" style="left:608px;top:2321px;width:505px;height:183px" role="img" aria-label="Gallery photograph: editorial group portrait"></div>
<div class="tile soft" style="left:608px;top:2519px;width:245px;height:183px" role="img" aria-label="Gallery photograph: group portrait"></div>
<div class="tile" style="left:868px;top:2519px;width:245px;height:183px" role="img" aria-label="Gallery photograph: editorial portrait"></div>

<footer class="abs footer">
  <p class="abs">© Copy Right -2017 Silver Lantern Studio.All rights reserved.</p>
  <span class="abs social" style="left:905px"></span>
  <span class="abs social" style="left:948px"></span>
  <span class="abs social" style="left:992px"></span>
  <span class="abs social" style="left:1035px"></span>
  <span class="abs social" style="left:1078px"></span>
</footer>

</body>
</html>
```